Electrical Contracting business card design

We need a simple business card design for an Electrical Contracting business. A simple design would be appreciated
This company has 2 directors so on one it would have Colin Marsh & another with Dana Marsh.
Updates

Reason: Hello A few designers have asked for a logo unfortunately we don't have one so have extended deadline to see who can help us out with this. CHEERS

Reason: Waiting for business partner to return from xmas break. cheers

Industry/Entity Type

Business

Contact Information for Business Card

Volmera Electrical Services P/L
REC: 36074
Residential Commercial Industrial
Service-Repairs-Renovations-Installations-Telephone-Data
Colin Marsh-Ph: 0433 517 862
Email: colin@volmeraelectrical.com.au

Requirements
Should not have
• The design should not have any electrical appliances in it ie: power-points, leads, houses etc.

```html
<!DOCTYPE html>
<html lang="en">
<head>
<meta charset="utf-8">
<title>Volmera Electrical Services – Business Card</title>
<link rel="stylesheet" href="https://fonts.googleapis.com/css2?family=Montserrat:wght@300;400&display=swap">
<style>
  :root {
    --ink: #333333;
    --teal: #2a9a8c;
    --orange: #ec7a3a;
    --paper: #ffffff;
  }
  html, body {
    margin: 0;
    padding: 0;
    overflow: hidden;
    background: var(--paper);
  }
  .card {
    position: relative;
    width: 1200px;
    height: 741px;
    background: var(--paper);
    font-family: "Montserrat", sans-serif;
    color: var(--ink);
    overflow: hidden;
  }
  .brand-dot {
    position: absolute;
    left: 570px;
    top: 200px;
    width: 60px;
    height: 60px;
    border-radius: 50%;
    background: var(--teal);
  }
  .rule {
    position: absolute;
    left: 219px;
    top: 315px;
    width: 763px;
    height: 3px;
    background: var(--orange);
  }
  .company-name {
    position: absolute;
    left: 0;
    top: 338px;
    width: 1200px;
    margin: 0;
    text-align: center;
    font-weight: 300;
    font-size: 40px;
    letter-spacing: 4px;
    line-height: 1;
    color: var(--ink);
  }
  .services {
    position: absolute;
    left: 0;
    top: 392px;
    width: 1200px;
    margin: 0;
    text-align: center;
    font-weight: 400;
    font-size: 23px;
    letter-spacing: 1.6px;
    line-height: 1;
    color: var(--teal);
  }
  .details {
    position: absolute;
    left: 0;
    top: 628px;
    width: 1200px;
    margin: 0;
    text-align: center;
    font-weight: 400;
    font-size: 18px;
    letter-spacing: 1.4px;
    line-height: 1;
    white-space: pre;
    color: var(--ink);
  }
  .email-band {
    position: absolute;
    left: 0;
    top: 661px;
    width: 1200px;
    height: 36px;
    background: var(--teal);
    color: var(--paper);
    font-weight: 400;
    font-size: 23px;
    letter-spacing: 1.6px;
    line-height: 36px;
    text-align: center;
  }
</style>
</head>
<body>
  <main class="card">
    <div class="brand-dot"></div>
    <div class="rule"></div>
    <h1 class="company-name">VOLMERA ELECTRICAL SERVICES</h1>
    <p class="services">REPAIRS-RENOVATIONS-INSTALLATIONS-TELEPHONE</p>
    <p class="details">P / L REC : 36074  RESIDENTIAL COMMERCIAL INDUSTRIAL DATA COLIN MARSH - PH: 0433 517 862</p>
    <div class="email-band">EMAIL: COLIN@VOLMERAELECTRICAL.COM.AU</div>
  </main>
</body>
</html>
```